Talvenridge

We are re-branding the company with a new logo (attached) which I would
like to go on one side of the card, and I have attached a file showing what
the old back side looked like, and I do like the characters that show the
phone, e-mails, etc., I don't like the current arrangement, and I want
something clean, clear and out of the box, as we are an aviation consulting
firm, and we work outside of the box.

```html
<!DOCTYPE html>
<html lang="en">
<head>
<meta charset="utf-8">
<title>Talvenridge – Business Card</title>
<link rel="stylesheet" href="https://fonts.googleapis.com/css2?family=Exo+2:wght@500;600&family=Titillium+Web:wght@400;600&display=swap">
<style>
  :root {
    --bg: #e4e4e6;
    --card: #ffffff;
    --ink: #3a3a3c;
    --panel: #3d3d40;
    --accent: #a3262b;
    --muted: #8a8a8e;
    --title: #3b4a9a;
    --on-dark: #f2f2f2;
  }
  * { margin: 0; padding: 0; box-sizing: border-box; }
  html, body { width: 1200px; height: 974px; overflow: hidden; }
  body {
    background: var(--bg);
    font-family: "Titillium Web", sans-serif;
    color: var(--ink);
    display: flex;
    flex-direction: column;
    align-items: center;
    justify-content: center;
    gap: 40px;
  }
  .card {
    position: relative;
    width: 760px;
    height: 434px;
    background: var(--card);
    overflow: hidden;
    box-shadow: 0 6px 18px rgba(0,0,0,.18);
  }
  .brand { display: flex; flex-direction: column; align-items: center; }
  .brand-row { display: flex; align-items: center; gap: 14px; }
  .brand-dot {
    width: 46px; height: 46px; border-radius: 50%;
    background: var(--accent);
  }
  .brand-name {
    font-family: "Exo 2", sans-serif;
    font-weight: 600;
    font-size: 48px;
    letter-spacing: 1px;
    color: var(--accent);
    line-height: 1;
  }
  .brand-tagline {
    margin-top: 6px;
    font-size: 12px;
    letter-spacing: 1.5px;
    color: var(--muted);
    text-transform: uppercase;
  }
  /* front */
  .card-front .brand {
    position: absolute; left: 0; right: 0; top: 160px;
  }
  .band { position: absolute; background: var(--accent); }
  .card-front .band-top { right: 60px; top: 0; width: 170px; height: 22px; }
  .card-front .band-bottom { left: 120px; bottom: 0; width: 190px; height: 22px; }
  /* back */
  .panel-side {
    position: absolute; right: 0; top: 0; width: 270px; height: 100%;
    background: var(--panel);
  }
  .panel-bottom {
    position: absolute; left: 0; bottom: 0; width: 100%; height: 150px;
    background: var(--panel);
  }
  .card-back .band-edge { right: 0; top: 150px; width: 14px; height: 150px; }
  .card-back .brand { position: absolute; left: 40px; top: 70px; width: 420px; }
  .person { position: absolute; left: 40px; top: 212px; }
  .person-name { font-size: 28px; font-weight: 600; letter-spacing: 1px; line-height: 1.1; }
  .person-title { font-size: 18px; color: var(--title); }
  .contact-list {
    list-style: none;
    position: absolute;
    display: flex; flex-direction: column; gap: 12px;
    color: var(--on-dark);
    font-size: 17px;
  }
  .contact-list.personal { left: 40px; top: 306px; }
  .contact-list.online { left: 520px; top: 50px; }
  .contact-list li { display: flex; align-items: center; gap: 14px; }
  .icon {
    width: 26px; height: 26px; background: var(--on-dark);
    display: flex; align-items: center; justify-content: center; flex: none;
  }
  .icon svg { width: 16px; height: 16px; }
</style>
</head>
<body>
  <section class="card card-front">
    <div class="band band-top"></div>
    <div class="brand">
      <div class="brand-row">
        <span class="brand-dot"></span>
        <span class="brand-name">Talvenridge</span>
      </div>
      <p class="brand-tagline">Aviation consulting beyond the box</p>
    </div>
    <div class="band band-bottom"></div>
  </section>

  <section class="card card-back">
    <div class="panel-side"></div>
    <div class="panel-bottom"></div>
    <div class="band band-edge"></div>

    <div class="brand">
      <div class="brand-row">
        <span class="brand-dot"></span>
        <span class="brand-name">Talvenridge</span>
      </div>
      <p class="brand-tagline">Aviation consulting beyond the box</p>
    </div>

    <div class="person">
      <p class="person-name">MARCUS HOLLEN</p>
      <p class="person-title">Managing Director</p>
    </div>

    <ul class="contact-list personal">
      <li><span class="icon"><svg viewBox="0 0 16 16"><path d="M8 1a5 5 0 0 0-5 5c0 4 5 9 5 9s5-5 5-9a5 5 0 0 0-5-5zm0 7a2 2 0 1 1 0-4 2 2 0 0 1 0 4z" fill="#3d3d40"/></svg></span>Harbor Lane 45</li>
      <li><span class="icon"><svg viewBox="0 0 16 16"><path d="M4 1l3 3-2 2c1 2 3 4 5 5l2-2 3 3-2 3C7 15 1 9 1 3z" fill="#3d3d40"/></svg></span>012 555 0147</li>
      <li><span class="icon"><svg viewBox="0 0 16 16"><rect x="1" y="3" width="14" height="10" fill="#3d3d40"/><path d="M1 3l7 6 7-6" stroke="#f2f2f2" stroke-width="1.4" fill="none"/></svg></span>mhollen@mailbox.com</li>
    </ul>

    <ul class="contact-list online">
      <li><span class="icon"><svg viewBox="0 0 16 16"><circle cx="8" cy="8" r="6" fill="none" stroke="#3d3d40" stroke-width="1.6"/><path d="M2 8h12M8 2c3 3 3 9 0 12M8 2c-3 3-3 9 0 12" stroke="#3d3d40" stroke-width="1.2" fill="none"/></svg></span>www.talvenridge.com</li>
      <li><span class="icon"><svg viewBox="0 0 16 16"><circle cx="8" cy="8" r="4" fill="#3d3d40"/></svg></span>www.chirpline.com</li>
      <li><span class="icon"><svg viewBox="0 0 16 16"><circle cx="8" cy="8" r="4" fill="#3d3d40"/></svg></span>www.friendwall.com</li>
    </ul>
  </section>
</body>
</html>
```